Brightfern Development Corporation
Can I please see design #42 with the symbols to designate the Phone, Fax, Email and Address? Thanks.
I also like the back of the business card on design 43-45.
I like the cards that do not have too much red and over power the business card. I do like the symbols to designate phone, fax, email, address and the website information. I would like some color on the card though. I do not like the cards that are all white.
The logo should be uploaded now. Off to a good start, but please don't forget the stationary. We are looking for letterhead, envelopes, etc.

```html
<!DOCTYPE html>
<html lang="en">
<head>
<meta charset="utf-8">
<title>Brightfern Development Services – Business Card</title>
<link rel="stylesheet" href="https://fonts.googleapis.com/css2?family=Arimo:wght@400;700&display=swap">
<style>
  :root {
    --backdrop: #e8e5e1;
    --card: #ffffff;
    --card-shade: #eeeeee;
    --brand-red: #d8392b;
    --charcoal: #4a4a4a;
    --text-grey: #555555;
    --ghost: #f6dedb;
  }
  html, body {
    margin: 0;
    padding: 0;
    width: 1200px;
    height: 1025px;
    overflow: hidden;
    background: var(--backdrop);
    font-family: "Arimo", Arial, sans-serif;
  }
  .canvas { position: relative; width: 1200px; height: 1025px; }
  .card {
    position: absolute;
    width: 603px;
    height: 347px;
    border-radius: 16px;
    overflow: hidden;
    background: linear-gradient(135deg, var(--card) 40%, var(--card-shade) 100%);
    box-shadow: 0 4px 14px rgba(0,0,0,0.18);
  }
  .card-back { left: 461px; top: 453px; }
  .card-front { left: 161px; top: 145px; z-index: 2; }
  .swoosh { position: absolute; inset: 0; }

  .wordmark { position: absolute; left: 36px; top: 42px; display: flex; align-items: center; gap: 10px; }
  .wordmark-square { width: 22px; height: 22px; background: var(--brand-red); }
  .wordmark-name { color: var(--charcoal); font-weight: 700; line-height: 1.05; }
  .wordmark-name .line-1 { display: block; font-size: 30px; letter-spacing: -0.5px; }
  .wordmark-name .line-2 { display: block; font-size: 12px; letter-spacing: 1.6px; text-transform: uppercase; }

  .contact-list { position: absolute; left: 38px; top: 190px; margin: 0; padding: 0; list-style: none;
    font-size: 11px; line-height: 17px; color: var(--text-grey); }
  .contact-list li { display: flex; align-items: center; gap: 6px; }
  .contact-list li.indent { padding-left: 16px; }
  .contact-icon { width: 10px; height: 10px; flex: none; fill: var(--brand-red); }

  .person { position: absolute; left: 300px; top: 205px; }
  .person-name { margin: 0; font-size: 16px; font-weight: 700; color: var(--brand-red); }
  .person-title { margin: 2px 0 0; font-size: 11px; color: var(--text-grey); }
  .front-web { position: absolute; left: 38px; top: 306px; font-size: 11px; color: var(--brand-red);
    display: flex; align-items: center; gap: 6px; }

  .ghost-name { position: absolute; left: 40px; top: 40px; font-size: 118px; font-weight: 700;
    color: var(--ghost); letter-spacing: -3px; }
  .back-wordmark { position: absolute; right: 36px; top: 250px; font-size: 26px; font-weight: 700; color: var(--brand-red); }
  .back-web { position: absolute; right: 36px; top: 298px; font-size: 14px; color: var(--text-grey); }
</style>
</head>
<body>
<main class="canvas">
  <section class="card card-back" aria-label="Card back">
    <div class="ghost-name" aria-hidden="true">Brightfern</div>
    <div class="back-wordmark">Brightfern</div>
    <div class="back-web">www.brightferndevelopment.net</div>
  </section>

  <section class="card card-front" aria-label="Card front">
    <svg class="swoosh" viewBox="0 0 603 347" width="603" height="347" aria-hidden="true">
      <path d="M360 0 C540 70 565 235 385 347 L415 347 C600 245 585 65 392 0 Z" fill="var(--charcoal)"/>
      <path d="M392 0 C585 65 600 245 415 347 L603 347 L603 0 Z" fill="var(--brand-red)"/>
    </svg>

    <div class="wordmark">
      <span class="wordmark-square"></span>
      <span class="wordmark-name">
        <span class="line-1">Brightfern</span>
        <span class="line-2">Development Services</span>
      </span>
    </div>

    <ul class="contact-list">
      <li>
        <svg class="contact-icon" viewBox="0 0 10 10" aria-label="Address"><path d="M5 0C3 0 1.5 1.5 1.5 3.4 1.5 6 5 10 5 10s3.5-4 3.5-6.6C8.5 1.5 7 0 5 0zm0 4.8a1.4 1.4 0 1 1 0-2.8 1.4 1.4 0 0 1 0 2.8z"/></svg>
        <span>4815 Cedar Ridge Drive</span>
      </li>
      <li class="indent">Austin, TX 78745</li>
      <li>
        <svg class="contact-icon" viewBox="0 0 10 10" aria-label="Phone"><path d="M2 0.5l1.8 1.9-.9 1.3c.6 1.3 1.5 2.2 2.9 2.9l1.3-.9L9.5 7.5 8.4 9.5C4 9.3.7 6 .5 1.6z"/></svg>
        <span>(512) 555-0148</span>
      </li>
      <li>
        <svg class="contact-icon" viewBox="0 0 10 10" aria-label="Fax"><path d="M2.5 0h4l1 1v2.5h-5zM0.5 4h9v4h-1.5V6.5h-6V8H.5zM3 7h4v3H3z"/></svg>
        <span>(512) 555-0162</span>
      </li>
      <li>
        <svg class="contact-icon" viewBox="0 0 10 10" aria-label="Email"><path d="M0 2h10v.6L5 5.6 0 2.6zM0 3.8l5 3 5-3V8.5H0z"/></svg>
        <span>dreyes@brightferndevelopment.net</span>
      </li>
    </ul>

    <div class="person">
      <p class="person-name">Daniel Reyes</p>
      <p class="person-title">Vice President</p>
    </div>

    <div class="front-web">
      <svg class="contact-icon" viewBox="0 0 10 10" aria-label="Website"><path d="M5 0a5 5 0 1 0 0 10A5 5 0 0 0 5 0zm0 1c.6.6 1.1 1.8 1.2 3.5H3.8C3.9 2.8 4.4 1.6 5 1zM1.1 5.5h1.7c.1 1.3.4 2.4.9 3.2A4 4 0 0 1 1.1 5.5zm0-1A4 4 0 0 1 3.7 1.3c-.5.8-.8 1.9-.9 3.2zM5 9c-.6-.6-1.1-1.8-1.2-3.5h2.4C6.1 7.2 5.6 8.4 5 9zm1.3-.3c.5-.8.8-1.9.9-3.2h1.7a4 4 0 0 1-2.6 3.2zm.9-4.2c-.1-1.3-.4-2.4-.9-3.2a4 4 0 0 1 2.6 3.2z"/></svg>
      <span>www.brightferndevelopment.net</span>
    </div>
  </section>
</main>
</body>
</html>
```